Video production company website

VistaKeel Productions is a video and photography production company serving many Fortune 500 clients traveling to Hawaii and International Destinations. Our primary focus is the Corporate and Incentive group market, and offer both photography and video services. In addition, we also create custom marketing, sales, art, and real estate productions.

Target Market(s)

Corporate Incentive Travel Groups

Industry/Entity Type

Videography

Number of Pages Required

4 page

Requirements
Must have
• see doc with content. This will ultimately be needed to be a wordpress design so we can update ourselves.
Nice to have
• sleek design, professional, cutting edge, modern
Should not have
• too much Hawaii Feel, some ok but we do travel international

```html
<!DOCTYPE html>
<html lang="en">
<head>
<meta charset="utf-8">
<title>VistaKeel Productions</title>
<link rel="stylesheet" href="https://fonts.googleapis.com/css2?family=Open+Sans:wght@400;600;700;800&display=swap">
<style>
:root{
  --blue:#2b7cc9;
  --blue-dark:#1f64a8;
  --gold:#e1a11c;
  --ink:#2d2d2d;
  --muted:#6a6a6a;
  --line:#d9d9d9;
  --topbar:#262626;
  --panel:#efefef;
  --white:#ffffff;
}
*{box-sizing:border-box;margin:0;padding:0}
html,body{width:1200px;height:3103px;overflow:hidden}
body{font-family:"Open Sans",Arial,sans-serif;color:var(--ink);background:var(--white);position:relative}
.abs{position:absolute}

/* top bar & header */
.topbar{left:0;top:0;width:1200px;height:37px;background:var(--topbar)}
.topbar .social{right:250px;top:7px;display:flex;gap:8px}
.dot{width:23px;height:23px;border-radius:50%;background:#bdbdbd;display:block}
.topbar .phone{right:82px;top:8px;color:#fff;font-size:15px;font-weight:600;display:flex;align-items:center;gap:8px}
.header{left:0;top:37px;width:1200px;height:118px;background:linear-gradient(#fff,#f4f4f4)}
.brand{left:78px;top:-20px;display:flex;flex-direction:column;align-items:center;width:190px}
.brand .mark{width:110px;height:110px;border-radius:50%;background:var(--white);border:5px solid #111}
.brand .name{margin-top:4px;font-size:12px;font-weight:800;color:#111;letter-spacing:.2px}
.book{left:880px;top:42px;height:36px;width:240px;background:var(--gold);border-radius:18px;color:#fff;font-weight:700;font-size:14px;display:flex;align-items:center;padding-left:58px}
.book .cal{left:-2px;top:-4px;width:44px;height:44px;border-radius:50%;background:var(--blue);border:3px solid #fff;display:flex;align-items:center;justify-content:center}

.nav{left:0;top:155px;width:1200px;height:44px;background:var(--blue);display:flex;padding-left:78px}
.nav a{color:#fff;text-decoration:none;font-size:13px;font-weight:700;height:44px;line-height:44px;padding:0 22px}
.nav a.active{background:var(--gold)}

/* hero */
.hero{left:0;top:199px;width:1200px;height:471px;background:linear-gradient(160deg,#4d6b3a 0%,#6f8f4d 35%,#3e5a30 70%,#7d8d5d 100%)}
.hero .arrow{top:190px;width:26px;height:40px;background:rgba(0,0,0,.55);display:flex;align-items:center;justify-content:center}
.hero .caption{left:0;bottom:0;width:1200px;height:58px;background:linear-gradient(transparent,rgba(0,0,0,.45));color:#fff;text-align:center;font-size:26px;font-weight:700;line-height:50px}

/* welcome */
.welcome{left:78px;top:740px;width:627px}
.welcome h1{font-size:25px;font-weight:800;color:var(--blue);padding-bottom:12px;border-bottom:1px solid var(--line)}
.welcome h1 span{color:var(--gold)}
.welcome h1 small{font-size:14px;font-weight:600;color:var(--ink)}
.welcome p{margin-top:18px;font-size:13px;line-height:22px;color:#333}
.feature{top:178px;display:flex;align-items:center;gap:14px;color:var(--blue);font-size:18px;font-weight:600}
.feature .ring{width:66px;height:66px;border-radius:50%;border:2px solid #ddd;display:flex;align-items:center;justify-content:center}

.inquiry{left:765px;top:718px;width:353px;height:297px;border:1px solid var(--line)}
.inquiry .tab{left:20px;top:-6px;width:313px;height:42px;background:#3b3b3b;color:#fff;font-weight:800;font-size:19px;text-align:center;line-height:42px}
.inquiry .tab span{color:var(--gold)}
.field{left:18px;width:315px;height:34px;background:#f2f2f2;border:1px solid #dcdcdc;font-size:11px;color:#777;padding:7px 8px}
.field b{color:#d33;font-weight:400}
.submit{left:18px;top:240px;width:130px;height:34px;background:var(--blue);color:#fff;font-weight:700;font-size:14px;text-align:center;line-height:34px}

/* services */
.services{left:0;top:1061px;width:1200px;height:476px;background:linear-gradient(#3a3936 0%,#45433c 40%,#2c3036 72%,#1f242b 100%)}
.services h2{left:0;top:40px;width:1200px;text-align:center;color:#fff;font-size:28px;font-weight:800}
h2 span.g{color:var(--gold)}
.services .rule{left:333px;top:90px;width:534px;height:1px;background:rgba(255,255,255,.35)}
.emblem{left:490px;top:152px;width:220px;height:220px;border-radius:50%;border:8px solid #c9a24a;background:radial-gradient(#4a7fb8,#1e4f85);display:flex;align-items:center;justify-content:center;color:#fff;font-size:24px;font-weight:700}
.svc{width:240px;color:#fff}
.svc h3{font-size:19px;font-weight:700}
.svc p{font-size:12.5px;line-height:20px;color:#e6e6e6;margin-top:4px}
.svc.l{text-align:right}
.svc-ico{width:58px;height:58px;display:flex;align-items:center;justify-content:center}
.connector{height:2px;background:var(--gold)}
.connector::after{content:"";position:absolute;width:10px;height:10px;border-radius:50%;background:var(--gold);top:-4px}
.connector.l::after{right:-4px}
.connector.r::after{left:-4px}

/* gallery */
.gallery-title{left:0;top:1580px;width:1200px;text-align:center;font-size:26px;font-weight:800;color:var(--blue)}
.gallery-rule{left:370px;top:1626px;width:460px;height:1px;background:var(--line)}
.filter{left:388px;top:1648px;display:flex;align-items:center;gap:10px;font-size:14px;font-weight:600}
.filter .btn{height:42px;line-height:40px;padding:0 14px;border:1px solid #ccc;font-size:13px;font-weight:400}
.filter .btn.on{background:var(--gold);border-color:var(--gold);color:#fff;font-weight:600;position:relative}
.filter .btn.on::after{content:"";position:absolute;left:50%;bottom:-8px;margin-left:-8px;border:8px solid transparent;border-bottom:0;border-top-color:var(--gold)}
.tile{overflow:hidden}
.play{left:50%;top:50%;transform:translate(-50%,-50%);width:52px;height:36px;border-radius:9px;background:rgba(20,20,20,.85);display:flex;align-items:center;justify-content:center}
.overlay{left:6px;top:6px;right:6px;bottom:6px;background:rgba(40,40,40,.72);border:2px solid rgba(255,255,255,.6);color:#fff;text-align:center;padding-top:20px}
.overlay h4{font-size:14px;font-weight:600}
.overlay p{font-size:12.5px;line-height:21px;margin-top:12px;padding:0 60px}
.pager{left:575px;top:2266px;display:flex;gap:4px}
.pager span{width:24px;height:24px;display:flex;align-items:center;justify-content:center}

/* testimonials */
.testimonials{left:0;top:2344px;width:1200px;height:408px;background:var(--panel)}
.testimonials h2{left:0;top:50px;width:1200px;text-align:center;font-size:26px;font-weight:800;color:var(--blue)}
.testimonials .rule{left:370px;top:98px;width:460px;height:1px;background:var(--line)}
.quote{top:142px;width:505px;height:140px;background:#fff;border-radius:6px;padding:18px 18px}
.quote h5{color:var(--blue);font-size:13px;font-weight:600}
.quote p{font-size:12.5px;line-height:20px;margin-top:4px;width:360px}
.quote .marks{right:26px;top:-6px;font-size:170px;line-height:170px;font-weight:800;color:#d8d8d8;font-family:"Open Sans",Arial,sans-serif}
.quote .tail{left:120px;bottom:-22px;border-left:0 solid transparent;border-right:40px solid transparent;border-top:22px solid #fff}
.avatar{width:100px;height:100px;border-radius:50%;border:5px solid #fff;box-shadow:0 1px 4px rgba(0,0,0,.25)}
.who{font-size:14px;font-weight:700;color:#333}
.who span{color:var(--gold);letter-spacing:2px}
.t-arrow{top:190px;width:32px;height:32px;border-radius:50%;background:#fff;border:1px solid #ccc;display:flex;align-items:center;justify-content:center}

/* footer */
.footer{left:0;top:2752px;width:1200px;height:296px;background:var(--blue)}
.footer h6{color:#fff;font-size:13px;font-weight:800;margin-bottom:18px}
.col{top:46px}
.links a{display:block;color:#fff;text-decoration:none;font-size:12.5px;line-height:25px}
.links a::before{content:"›";margin-right:6px}
.contact div{color:#fff;font-size:12.5px;display:flex;gap:10px;margin-bottom:18px;line-height:16px}
.map{width:235px;height:140px;border:3px solid #fff;background:linear-gradient(135deg,#cfe0ee,#e9e7dc 50%,#bcd4e8)}
.follow .row{display:flex;gap:10px}
.follow .dot{width:28px;height:28px;background:var(--gold)}
.faint{left:990px;top:150px;width:90px;height:90px;border-radius:50%;border:5px solid rgba(255,255,255,.45);display:flex;align-items:center;justify-content:center;color:rgba(255,255,255,.55);font-size:13px;font-weight:700}
.copy{left:0;top:3048px;width:1200px;height:55px;background:var(--gold);color:#fff;text-align:center;line-height:55px;font-size:13px;font-weight:600}
</style>
</head>
<body>

<div class="abs topbar">
  <div class="abs social"><i class="dot"></i><i class="dot"></i><i class="dot"></i><i class="dot"></i></div>
  <div class="abs phone">
    <svg width="14" height="14" viewBox="0 0 24 24"><path fill="#fff" d="M6.6 10.8a15 15 0 0 0 6.6 6.6l2.2-2.2c.3-.3.7-.4 1-.2 1.1.4 2.3.6 3.6.6.6 0 1 .4 1 1V20c0 .6-.4 1-1 1A17 17 0 0 1 3 4c0-.6.4-1 1-1h3.5c.6 0 1 .4 1 1 0 1.3.2 2.5.6 3.6.1.3 0 .7-.2 1z"/></svg>
    (555) 014.2290
  </div>
</div>

<header class="abs header">
  <div class="abs brand" style="top:-28px">
    <div class="mark"></div>
    <div class="name">VISTAKEEL PRODUCTIONS</div>
  </div>
  <div class="abs book">
    <span class="abs cal"><svg width="20" height="20" viewBox="0 0 24 24"><rect x="3" y="5" width="18" height="16" rx="2" fill="none" stroke="#fff" stroke-width="2"/><path d="M3 10h18M8 3v4M16 3v4" stroke="#fff" stroke-width="2"/></svg></span>
    BOOK YOUR SERVICE
  </div>
</header>

<nav class="abs nav">
  <a class="active">HOME</a><a>ABOUT US</a><a>VIDEOGRAPHY</a><a>PHOTOGRAPHY</a><a>WHY CHOOSE US</a><a>TESTIMONIALS</a><a>CONTACT US</a>
</nav>

<section class="abs hero" role="img" aria-label="Photo of a corporate group at an outdoor garden evening event with lanterns and palm trees">
  <div class="abs arrow" style="left:0"><svg width="10" height="14"><path d="M8 1 2 7l6 6" stroke="#fff" stroke-width="2" fill="none"/></svg></div>
  <div class="abs arrow" style="right:0"><svg width="10" height="14"><path d="m2 1 6 6-6 6" stroke="#fff" stroke-width="2" fill="none"/></svg></div>
  <div class="abs caption">The Best of the Best</div>
</section>

<section class="abs welcome">
  <h1>WELCOME TO <span>VISTAKEEL PRODUCTIONS</span> <small>LLC</small></h1>
  <p>VistaKeel Productions is a video and photography production company serving many Fortune 500 clients in Hawaii and Internationally. Our primary focus is the Corporate and Incentive group market, and offer both photography and video services. In addition, we also create custom marketing, sales, art, and real estate productions.</p>
  <div class="abs feature" style="left:0">
    <span class="ring"><svg width="34" height="28" viewBox="0 0 34 28"><rect x="2" y="12" width="20" height="13" rx="2" fill="var(--gold)"/><circle cx="7" cy="6" r="5" fill="none" stroke="var(--gold)" stroke-width="2.5"/><circle cx="17" cy="6" r="5" fill="none" stroke="var(--gold)" stroke-width="2.5"/><path d="M22 16l9-5v15l-9-5z" fill="var(--blue)"/></svg></span>
    Videography
  </div>
  <div class="abs feature" style="left:295px">
    <span class="ring"><svg width="32" height="26" viewBox="0 0 32 26"><rect x="1" y="6" width="30" height="19" rx="3" fill="var(--gold)"/><rect x="10" y="2" width="12" height="6" rx="1" fill="var(--gold)"/><circle cx="16" cy="15" r="6" fill="#fff"/><circle cx="16" cy="15" r="3.5" fill="var(--blue)"/></svg></span>
    Photography
  </div>
</section>

<aside class="abs inquiry">
  <div class="abs tab">QUICK <span>INQUIRY</span></div>
  <div class="abs field" style="top:56px">Name <b>*</b></div>
  <div class="abs field" style="top:98px">Email <b>*</b></div>
  <div class="abs field" style="top:140px;height:80px">Message <b>*</b></div>
  <div class="abs submit">SUBMIT</div>
</aside>

<section class="abs services" role="img" aria-label="Photo of a sunset over the ocean with mountains on the horizon">
  <h2 class="abs">OUR OTHER <span class="g">SERVICES</span></h2>
  <div class="abs rule"></div>
  <div class="abs emblem">VistaKeel</div>

  <div class="abs svc l" style="left:78px;top:172px"><h3>Real Estate Productions</h3><p>Lorem ipsum dolor sit amet, consectetuer Lorem ipsum dolor sit amet adipiscing el ...</p></div>
  <div class="abs svc-ico" style="left:320px;top:170px"><svg width="48" height="48" viewBox="0 0 48 48" fill="none" stroke="#fff" stroke-width="3"><path d="M6 22 24 6l18 16"/><path d="M12 18v22h24V18"/><circle cx="24" cy="27" r="5"/></svg></div>
  <div class="abs connector l" style="left:385px;top:198px;width:75px"></div>

  <div class="abs svc l" style="left:78px;top:318px"><h3>Art</h3><p>Lorem ipsum dolor sit amet, consectetuer Lorem ipsum dolor sit amet adipiscing el ...</p></div>
  <div class="abs svc-ico" style="left:320px;top:316px"><svg width="48" height="48" viewBox="0 0 48 48"><path d="M24 6a18 18 0 1 0 0 36c3 0 3-3 1-5-2-2 0-5 3-5h5a9 9 0 0 0 9-9C42 13 34 6 24 6z" fill="#fff"/><circle cx="15" cy="20" r="3" fill="#333"/><circle cx="22" cy="13" r="3" fill="#333"/><circle cx="31" cy="15" r="3" fill="#333"/></svg></div>
  <div class="abs connector l" style="left:385px;top:344px;width:75px"></div>

  <div class="abs connector r" style="left:740px;top:198px;width:75px"></div>
  <div class="abs svc-ico" style="left:820px;top:170px"><svg width="48" height="48" viewBox="0 0 48 48" fill="none" stroke="#fff" stroke-width="3"><rect x="5" y="9" width="38" height="30" rx="2"/><path d="M20 17l11 7-11 7z" fill="#fff"/></svg></div>
  <div class="abs svc" style="left:883px;top:172px"><h3>Custom Marketing</h3><p>Lorem ipsum dolor sit amet, consectetuer Lorem ipsum dolor sit amet adipiscing el ...</p></div>

  <div class="abs connector r" style="left:740px;top:344px;width:75px"></div>
  <div class="abs svc-ico" style="left:820px;top:316px"><svg width="48" height="48" viewBox="0 0 48 48"><path d="M6 8h18l18 18-16 16L6 24z" fill="#fff"/><circle cx="15" cy="17" r="3.5" fill="#333"/></svg></div>
  <div class="abs svc" style="left:883px;top:318px"><h3>Sales</h3><p>Lorem ipsum dolor sit amet, consectetuer Lorem ipsum dolor sit amet adipiscing el ...</p></div>
</section>

<h2 class="abs gallery-title">OUR <span class="g">GALLERY</span></h2>
<div class="abs gallery-rule"></div>
<div class="abs filter">FILTER <span class="btn on" style="margin-left:14px">ALL</span><span class="btn">PHOTOGRAPHY</span><span class="btn">VIDEOGRAPHY</span></div>

<div class="abs tile" style="left:78px;top:1709px;width:267px;height:317px;background:linear-gradient(#6f9bc4,#2f6fa8)" role="img" aria-label="Photo of a banquet set with blue tablecloths beside a resort"></div>
<div class="abs tile" style="left:349px;top:1709px;width:499px;height:150px;background:linear-gradient(#6a6a62,#3c3b38)" role="img" aria-label="Photo of a group gathering">
  <div class="abs overlay"><h4>Lorem ipsum dolor sit amet</h4><p>Lorem ipsum dolor sit amet, consectetuer adipiscing elit, sed diam nonummy nibh euismod tincidunt ut</p>
    <svg class="abs" style="left:50%;margin-left:-12px;bottom:12px" width="24" height="24" viewBox="0 0 24 24"><circle cx="12" cy="12" r="10" fill="none" stroke="#fff" stroke-width="2"/><path d="M12 7v10M7 12h10" stroke="#fff" stroke-width="2"/></svg>
  </div>
</div>
<div class="abs tile" style="left:349px;top:1864px;width:247px;height:162px;background:linear-gradient(#38c0cc,#1d8fa6)" role="img" aria-label="Video still of a person jumping into turquoise water">
  <div class="abs play"><svg width="14" height="16"><path d="M1 1l12 7-12 7z" fill="#fff"/></svg></div>
</div>
<div class="abs tile" style="left:601px;top:1864px;width:247px;height:162px;background:linear-gradient(#3a2a2a,#8a4a3a)" role="img" aria-label="Photo of guests posing under a neon welcome sign at night"></div>
<div class="abs tile" style="left:853px;top:1709px;width:265px;height:317px;background:linear-gradient(#f0a43a 0%,#c56a2c 35%,#4a6c8e 70%,#e2d7c8 100%)" role="img" aria-label="Photo of a sunset dinner table set on a beach"></div>
<div class="abs tile" style="left:78px;top:2032px;width:522px;height:216px;background:linear-gradient(#a7c2d8 0%,#8aa27a 40%,#3b3b3b 75%,#6b4a8a 100%)" role="img" aria-label="Photo of a large corporate group on a riverboat deck"></div>
<div class="abs tile" style="left:604px;top:2032px;width:514px;height:216px;background:linear-gradient(#9ab2c4,#dfe6ea 55%,#c7b79a)" role="img" aria-label="Video still of a young surfer in shallow waves">
  <div class="abs play"><svg width="14" height="16"><path d="M1 1l12 7-12 7z" fill="#fff"/></svg></div>
</div>
<div class="abs pager">
  <span style="background:#bbb"><svg width="12" height="12"><path d="M8 2 3 6l5 4" stroke="#fff" stroke-width="2" fill="none"/></svg></span>
  <span style="background:#222"><svg width="12" height="12"><path d="m4 2 5 4-5 4" stroke="#fff" stroke-width="2" fill="none"/></svg></span>
</div>

<section class="abs testimonials">
  <h2 class="abs">CLIENT <span class="g">TESTIMONIALS</span></h2>
  <div class="abs rule"></div>
  <div class="abs t-arrow" style="left:21px"><svg width="10" height="12"><path d="M7 1 2 6l5 5" stroke="#888" stroke-width="1.5" fill="none"/></svg></div>
  <div class="abs t-arrow" style="left:1145px"><svg width="10" height="12"><path d="m3 1 5 5-5 5" stroke="#888" stroke-width="1.5" fill="none"/></svg></div>

  <div class="abs quote" style="left:78px">
    <div class="abs marks">"</div>
    <h5>Lorem ipsum dolor sit amet, consectet uer</h5>
    <p>Lorem ipsum dolor sit amet, consectet uer adipiscing elit, sed diam nonummy nibh euis mod tincidun nt ut laoreetmi dolore magna aliquam erat volutpat.</p>
    <div class="abs tail"></div>
  </div>
  <div class="abs avatar" style="left:104px;top:258px;background:linear-gradient(#8fb3d6,#d9c7a8)" role="img" aria-label="Portrait photo of the client"></div>
  <div class="abs who" style="left:300px;top:318px">- Miss Lena Okafor <span>★★★★★</span></div>

  <div class="abs quote" style="left:613px">
    <div class="abs marks">"</div>
    <h5>Lorem ipsum dolor sit amet, consectet uer</h5>
    <p>Lorem ipsum dolor sit amet, consectet uer adipiscing elit, sed diam nonummy nibh euis mod tincidun nt ut laoreetmi dolore magna aliquam erat volutpat.</p>
    <div class="abs tail"></div>
  </div>
  <div class="abs avatar" style="left:640px;top:258px;background:linear-gradient(#c9a37a,#6f8fa8)" role="img" aria-label="Portrait photo of the client"></div>
  <div class="abs who" style="left:860px;top:318px">Mr. Quis Nostrud Exerci <span>★★★★★</span></div>
</section>

<footer class="abs footer">
  <div class="abs col links" style="left:82px">
    <h6>QUICK LINKS</h6>
    <a>Home</a><a>About Us</a><a>Videography</a><a>Photography</a><a>Why Choose Us</a><a>Testimonials</a><a>Contact Us</a>
  </div>
  <div class="abs col contact" style="left:293px">
    <h6>CONTACT DETAILS</h6>
    <div><svg width="12" height="16" viewBox="0 0 12 16"><path d="M6 0a6 6 0 0 0-6 6c0 4.5 6 10 6 10s6-5.5 6-10a6 6 0 0 0-6-6z" fill="var(--gold)"/><circle cx="6" cy="6" r="2.2" fill="var(--blue)"/></svg><span><b>VistaKeel Productions, LLC</b><br>P.O. Box 410-227</span></div>
    <div><svg width="14" height="14" viewBox="0 0 24 24"><path fill="var(--gold)" d="M6.6 10.8a15 15 0 0 0 6.6 6.6l2.2-2.2c.3-.3.7-.4 1-.2 1.1.4 2.3.6 3.6.6.6 0 1 .4 1 1V20c0 .6-.4 1-1 1A17 17 0 0 1 3 4c0-.6.4-1 1-1h3.5c.6 0 1 .4 1 1 0 1.3.2 2.5.6 3.6.1.3 0 .7-.2 1z"/></svg><b>(555) 014.2290</b></div>
    <div><svg width="14" height="14" viewBox="0 0 24 24"><path fill="var(--gold)" d="M6.6 10.8a15 15 0 0 0 6.6 6.6l2.2-2.2c.3-.3.7-.4 1-.2 1.1.4 2.3.6 3.6.6.6 0 1 .4 1 1V20c0 .6-.4 1-1 1A17 17 0 0 1 3 4c0-.6.4-1 1-1h3.5c.6 0 1 .4 1 1 0 1.3.2 2.5.6 3.6.1.3 0 .7-.2 1z"/></svg><b>(555) 014.2290</b></div>
    <div><svg width="16" height="12" viewBox="0 0 16 12"><rect width="16" height="12" rx="1" fill="var(--gold)"/><path d="m1 1 7 6 7-6" stroke="var(--blue)" stroke-width="1.5" fill="none"/></svg>info@vistakeelproductions.com</div>
  </div>
  <div class="abs col" style="left:615px">
    <h6>LOCATION MAP</h6>
    <div class="map" role="img" aria-label="Street map showing the office location"></div>
  </div>
  <div class="abs col follow" style="left:955px">
    <h6>FOLLOW US</h6>
    <div class="row"><i class="dot"></i><i class="dot"></i><i class="dot"></i><i class="dot"></i></div>
  </div>
  <div class="abs faint">VistaKeel</div>
</footer>
<div class="abs copy">Copyright © 2016 VistaKeel Productions. All Rights Reserved.</div>

</body>
</html>
```